Dr. Pelma Antarctic Pelma Oil

We need a bottle label design for a new company called Dr. Pelma. We sell Pelma Oil in gel caps. Krill are shrimp-like crustaceans. We are looking for a professional concept that communicates the essence of ocean, health, life, purity...maybe a krill with medical authority.

There are a few labels out there. I attached 2. Dr. Vostin has some nice vector krill art, though the label is otherwise sparse. Amber Ridge has the feel of a nice full line of professional products, though there's nothing particularly krilly about it. Could there be a happy marriage of the two?

What we do NOT want is a photograph of an ocean with words over it. That screams Japanese karaoke.

Auxiliary wording on label front:
Heart Health
Antarctic
100% Pure
Dietary Supplements
1000mg

I apologize to designers for my new-to-crowd-design vagueness above, but I will try to be very forthcoming with feedback.

Thank you all!

Target Market(s)

Pelma Oil buyers. The 40+ crowd who want their Omega 3s and know that Pelma Oil has it in spades!

Industry/Entity Type

It Company

Requirements
Nice to have
• A singular image that can be lifted for website branding as well...

```html
<!DOCTYPE html>
<html lang="en">
<head>
<meta charset="utf-8">
<title>Dr. Pelma Antarctic Pelma Oil – Bottle Label</title>
<link href="https://fonts.googleapis.com/css2?family=Arimo:wght@400;700&display=swap" rel="stylesheet">
<style>
  :root {
    --brand-blue: #1b5c9e;
    --deep-blue: #16508c;
    --gold: #dba833;
    --ice-blue: #8cc8ea;
    --ink: #1d3f66;
    --panel-grey: #d4d4d4;
    --frame: #c9c9c9;
    --paper: #ffffff;
  }
  * { margin: 0; padding: 0; box-sizing: border-box; }
  html, body { width: 1200px; height: 806px; overflow: hidden; background: var(--paper); }
  body { position: relative; font-family: "Arimo", Arial, sans-serif; color: var(--ink); }

  .variant-tag { position: absolute; font-size: 38px; color: #222; font-weight: 400; }
  .variant-tag.a { left: 2px; top: 48px; }
  .variant-tag.b { left: 2px; top: 440px; }

  .label { position: absolute; width: 1162px; height: 381px; border: 1px solid var(--frame); background: var(--paper); }
  .label.a { left: 35px; top: 5px; }
  .label.b { left: 30px; top: 422px; }
  .label > * { position: absolute; }

  /* Supplement facts */
  .facts { left: 20px; top: 13px; width: 240px; height: 270px; border: 1px solid var(--brand-blue); padding: 12px 8px 0; font-size: 9.5px; color: var(--ink); }
  .facts h2 { text-align: center; font-size: 17px; line-height: 20px; font-weight: 700; color: var(--brand-blue); letter-spacing: .3px; margin-bottom: 8px; }
  .facts .row { display: flex; justify-content: space-between; font-size: 8.5px; line-height: 12px; margin-bottom: 3px; white-space: nowrap; padding: 0 4px; }
  .facts .rule { height: 4px; background: var(--brand-blue); margin: 4px 0 10px; }
  .facts ul { list-style: none; }
  .facts li { line-height: 17px; }
  .facts .rule.bottom { height: 8px; margin: 4px 0 6px; }
  .facts .note { font-size: 8.6px; line-height: 11px; padding-left: 4px; white-space: nowrap; }

  .other-ingredients { left: 20px; top: 291px; font-size: 9.5px; line-height: 1.3; color: var(--ink); }
  .other-ingredients b { color: var(--brand-blue); }

  .mini-mark { left: 68px; top: 316px; width: 150px; text-align: center; line-height: 1; }
  .mini-mark .pre { font-size: 9px; letter-spacing: 3px; color: var(--brand-blue); }
  .mini-mark .name { font-size: 21px; font-weight: 700; color: var(--brand-blue); margin: 2px 0; }
  .mini-mark .tag { font-size: 9px; letter-spacing: 2px; color: var(--gold); font-weight: 700; }

  /* Front panel */
  .brand-block { left: 310px; top: 0; width: 82px; height: 60px; background: var(--brand-blue); display: flex; align-items: center; justify-content: center; color: #fff; font-weight: 700; font-size: 16px; }
  .hero-art { left: 285px; top: 8px; width: 525px; height: 182px;
    background: radial-gradient(ellipse 40px 90px at 50% 48%, var(--gold) 0 98%, transparent 100%),
                linear-gradient(180deg, transparent 50%, var(--ice-blue) 52%, #cde7f6 85%, transparent 90%); opacity: .9; }
  .purity-seal { left: 712px; top: 14px; width: 64px; height: 58px; border-right: 3px solid var(--gold); border-radius: 50%; text-align: center; padding-top: 12px; line-height: 1; }
  .purity-seal .pct { color: var(--gold); font-size: 14px; font-weight: 700; }
  .purity-seal .word { color: var(--brand-blue); font-size: 24px; font-weight: 700; }

  .origin-line { left: 285px; top: 197px; width: 527px; display: flex; align-items: center; gap: 12px; color: var(--brand-blue); font-size: 18px; letter-spacing: 5px; font-weight: 400; }
  .origin-line::before, .origin-line::after { content: ""; flex: 1; height: 2px; background: var(--brand-blue); }
  .product-name { left: 285px; top: 218px; width: 527px; text-align: center; font-size: 64px; font-weight: 700; color: var(--brand-blue); letter-spacing: 1px; line-height: 1; }
  .benefit-band { left: 283px; top: 285px; width: 527px; height: 32px; background: var(--brand-blue); color: #fff; text-align: center; font-size: 19px; letter-spacing: 4px; font-weight: 700; line-height: 32px; }
  .category-band { left: 283px; top: 317px; width: 527px; height: 63px; background: var(--gold); overflow: hidden; }
  .category-band .cat { position: absolute; left: 25px; top: 22px; color: #fff; font-weight: 700; font-size: 21px; }
  .category-band svg { position: absolute; right: 0; bottom: 0; }
  .category-band .dose { position: absolute; right: 42px; bottom: 7px; color: #fff; font-size: 17px; }

  /* Back panel */
  .directions { left: 825px; top: 12px; width: 226px; font-size: 9.6px; line-height: 1.45; color: var(--ink); }
  .directions p { margin-bottom: 9px; text-align: justify; }
  .directions b { color: var(--brand-blue); }
  .disclaimer { left: 822px; top: 202px; width: 228px; height: 74px; border: 1px solid var(--brand-blue); padding: 5px 7px; font-size: 9.6px; line-height: 1.45; }
  .disclaimer b { color: var(--brand-blue); }
  .distributor { left: 825px; top: 285px; font-size: 12.4px; line-height: 20.5px; color: var(--ink); }
  .code-panel { left: 1065px; top: 13px; width: 85px; height: 265px; background: var(--panel-grey); }
</style>
</head>
<body>

<span class="variant-tag a">A</span>
<span class="variant-tag b">B</span>

<section class="label a">
  <div class="facts">
    <h2>SUPPLEMENT FACTS</h2>
    <div class="row"><span>Serving Size : 2 softgels</span><span>Serving per container : 30</span></div>
    <div class="row"><span>Amount per Serving :</span><span>%DV*</span></div>
    <div class="rule"></div>
    <ul>
      <li>Vitamin A</li>
      <li>Nereid Pelma Oil (NPO)</li>
      <li>Phospholipiods, omega -3 rich</li>
      <li>Eicosapentaenoic acid (EPA)</li>
      <li>Docosahexaenoic Acis (DHA)</li>
      <li>Omega-6 fatty acids, total</li>
      <li>Transfat</li>
      <li>Astaxanthin</li>
    </ul>
    <div class="rule bottom"></div>
    <p class="note">*Percent Daily Values based on a 2,000 calorie diet<br>** Daily Value not established</p>
  </div>
  <p class="other-ingredients"><b>Other ingredients :</b> Gelatin (capsule),glycerin &amp; water.<br><b>Expiration Date :</b></p>
  <div class="mini-mark"><div class="pre">ANTARCTIC</div><div class="name">PELMA OIL</div><div class="tag">HEART HEALTH</div></div>

  <div class="hero-art" role="img" aria-label="Illustration of a crustacean inside a golden oil drop over pale blue Antarctic mountains"></div>
  <div class="brand-block">Dr. Pelma</div>
  <div class="purity-seal"><div class="pct">100%</div><div class="word">pure</div></div>
  <div class="origin-line">ANTARCTIC</div>
  <div class="product-name">PELMA OIL</div>
  <div class="benefit-band">HEART HEALTH</div>
  <div class="category-band">
    <span class="cat">DIETARY SUPPLEMENT</span>
    <svg width="140" height="34" viewBox="0 0 140 34"><path d="M0 34 C12 34 14 0 30 0 H140 V34 Z" fill="var(--brand-blue)"/></svg>
    <span class="dose">1000mg</span>
  </div>

  <div class="directions">
    <p><b>Suggested Use</b> : 2 Softgels daily with the first meal.</p>
    <p><b>Warning</b> : If you are allergic to shellfish, have a blood coagulation condition, or are taking anticoagulants sch as Warfarin (Clotrin). Consult a health care professional prior to use.</p>
    <p>NPO is a extract from Antarctical that is rich in cell membrane building blocks : highly unsaturated phosolipids co-functionalized with omega-3 fatty acids (EPA &amp; DHA). Although benifitioual for both men &amp; women, NPO also supports relief of PMS Symptoms.*</p>
  </div>
  <div class="disclaimer"><b>Suggested Use</b> : 2 Softgels daily with the first These Statements have been approved by the FDA. This product is not intended to diagnose, treat, Cureor Prevent any disease.</div>
  <div class="distributor">Distributed by :<br>customer services @<br>address State pin code<br>Contact : 0000 000 0000</div>
  <div class="code-panel"></div>
</section>

<section class="label b">
  <div class="facts">
    <h2>SUPPLEMENT FACTS</h2>
    <div class="row"><span>Serving Size : 2 softgels</span><span>Serving per container : 30</span></div>
    <div class="row"><span>Amount per Serving :</span><span>%DV*</span></div>
    <div class="rule"></div>
    <ul>
      <li>Vitamin A</li>
      <li>Nereid Pelma Oil (NPO)</li>
      <li>Phospholipiods, omega -3 rich</li>
      <li>Eicosapentaenoic acid (EPA)</li>
      <li>Docosahexaenoic Acis (DHA)</li>
      <li>Omega-6 fatty acids, total</li>
      <li>Transfat</li>
      <li>Astaxanthin</li>
    </ul>
    <div class="rule bottom"></div>
    <p class="note">*Percent Daily Values based on a 2,000 calorie diet<br>** Daily Value not established</p>
  </div>
  <p class="other-ingredients"><b>Other ingredients :</b> Gelatin (capsule),glycerin &amp; water.<br><b>Expiration Date :</b></p>
  <div class="mini-mark"><div class="pre">ANTARCTIC</div><div class="name">PELMA OIL</div><div class="tag">HEART HEALTH</div></div>

  <div class="hero-art" role="img" aria-label="Illustration of a crustacean inside a golden oil drop over pale blue Antarctic mountains"></div>
  <div class="brand-block">Dr. Pelma</div>
  <div class="purity-seal"><div class="pct">100%</div><div class="word">pure</div></div>
  <div class="origin-line">ANTARCTIC</div>
  <div class="product-name">PELMA OIL</div>
  <div class="benefit-band">HEART HEALTH</div>
  <div class="category-band">
    <span class="cat">DIETARY SUPPLEMENT</span>
    <svg width="140" height="34" viewBox="0 0 140 34"><path d="M0 34 C12 34 14 0 30 0 H140 V34 Z" fill="var(--brand-blue)"/></svg>
    <span class="dose">1000mg</span>
  </div>

  <div class="directions">
    <p><b>Suggested Use</b> : 2 Softgels daily with the first meal.</p>
    <p><b>Warning</b> : If you are allergic to shellfish, have a blood coagulation condition, or are taking anticoagulants sch as Warfarin (Clotrin). Consult a health care professional prior to use.</p>
    <p>NPO is a extract from Antarctical that is rich in cell membrane building blocks : highly unsaturated phosolipids co-functionalized with omega-3 fatty acids (EPA &amp; DHA). Although benifitioual for both men &amp; women, NPO also supports relief of PMS Symptoms.*</p>
  </div>
  <div class="disclaimer"><b>Suggested Use</b> : 2 Softgels daily with the first These Statements have been approved by the FDA. This product is not intended to diagnose, treat, Cureor Prevent any disease.</div>
  <div class="distributor">Distributed by :<br>customer services @<br>address State pin code<br>Contact : 0000 000 0000</div>
  <div class="code-panel"></div>
</section>

</body>
</html>
```